Q&L Summit Holdings Business Cards

Design Business cards in a format where I can change the information and utilize a third party buisness card printing company

Contact Information for Business Card

Want Logo and Name on Back. Looking for Spot UV style shine on Logo. Probably Black background. Want smaller logo on front with contact details. Like rounded edges or something else interesting.

Requirements
Must have
• Strong masculine look.

```html
<!DOCTYPE html>
<html lang="en">
<head>
<meta charset="utf-8">
<title>Q&amp;L Summit Holdings Business Cards</title>
<link rel="stylesheet" href="https://fonts.googleapis.com/css2?family=Cinzel:wght@400&family=Open+Sans:wght@400&display=swap">
<style>
  :root {
    --stage: #1c1c1c;
    --card: #141414;
    --card-edge: #262626;
    --silver: #d9d9d9;
    --grey: #8e8e8e;
    --text: #c9c9c9;
    --rule: #3a3a3a;
  }
  * { box-sizing: border-box; margin: 0; padding: 0; }
  html, body { width: 1200px; height: 900px; overflow: hidden; }
  body {
    background: var(--stage);
    font-family: "Open Sans", Arial, sans-serif;
    color: var(--text);
    position: relative;
  }
  .card {
    position: absolute;
    left: 320px;
    width: 560px;
    height: 320px;
    background: var(--card);
    border: 1px solid var(--card-edge);
    border-radius: 22px;
    box-shadow: 0 18px 40px rgba(0,0,0,0.55);
  }
  .card-back { top: 110px; }
  .card-front { top: 470px; }

  /* back */
  .back-brand {
    position: absolute;
    top: 100px; left: 0; right: 0;
    display: flex; align-items: center; justify-content: center; gap: 16px;
  }
  .brand-square {
    width: 34px; height: 34px;
    background: var(--silver);
  }
  .brand-name {
    font-family: "Cinzel", Georgia, serif;
    font-weight: 400;
    font-size: 34px;
    letter-spacing: 1px;
    color: var(--silver);
  }
  .back-web {
    position: absolute;
    top: 190px; left: 0; right: 0;
    text-align: center;
    font-size: 13px;
    letter-spacing: 4px;
    color: #f0f0f0;
  }

  /* front */
  .front-brand {
    position: absolute;
    top: 48px; right: 40px;
    display: flex; align-items: center; gap: 10px;
  }
  .front-brand .brand-square { width: 20px; height: 20px; background: var(--grey); }
  .front-brand .brand-name { font-size: 22px; color: var(--grey); }
  .front-rule {
    position: absolute;
    top: 100px; left: 40px; right: 40px;
    height: 1px; background: var(--rule);
  }
  .address {
    position: absolute;
    top: 116px; right: 40px;
    text-align: right;
    font-size: 13px;
    line-height: 20px;
    color: var(--text);
  }
  .person { position: absolute; left: 40px; top: 160px; }
  .person-name {
    font-family: "Cinzel", Georgia, serif;
    font-size: 20px;
    color: var(--grey);
    letter-spacing: 0.5px;
  }
  .person-title { font-size: 13px; color: var(--text); margin-top: 2px; }
  .person-rule { width: 210px; height: 1px; background: var(--rule); margin: 10px 0 10px; }
  .contact-list { list-style: none; }
  .contact-list li {
    display: flex; align-items: center; gap: 8px;
    font-size: 13px; line-height: 20px; color: var(--text);
  }
  .contact-list svg { width: 12px; height: 12px; fill: var(--grey); flex: none; }
</style>
</head>
<body>

<section class="card card-back" aria-label="Card back">
  <div class="back-brand">
    <span class="brand-square"></span>
    <span class="brand-name">Q&amp;L Summit Holdings</span>
  </div>
  <p class="back-web">www.qlsummitholdings.com</p>
</section>

<section class="card card-front" aria-label="Card front">
  <div class="front-brand">
    <span class="brand-square"></span>
    <span class="brand-name">Q&amp;L Summit Holdings</span>
  </div>
  <div class="front-rule"></div>
  <p class="address">12345, Address Goes Here<br>Country Name, 123456</p>

  <div class="person">
    <p class="person-name">DANIEL REEVE</p>
    <p class="person-title">Managing Director</p>
    <div class="person-rule"></div>
    <ul class="contact-list">
      <li>
        <svg viewBox="0 0 12 12" aria-hidden="true"><path d="M1 4c0-1.5 2-3 5-3s5 1.5 5 3v1H8.5V3.8h-5V5H1zM2.5 6h7L11 11H1z"/></svg>
        044-555 018 274
      </li>
      <li>
        <svg viewBox="0 0 12 12" aria-hidden="true"><path d="M3.5 0h5a1 1 0 0 1 1 1v10a1 1 0 0 1-1 1h-5a1 1 0 0 1-1-1V1a1 1 0 0 1 1-1zm.5 1.5v7.5h4V1.5z"/></svg>
        044-555 018 274
      </li>
      <li>
        <svg viewBox="0 0 12 12" aria-hidden="true"><path d="M0 2.5h12v7H0zM0.8 3.2L6 7l5.2-3.8V3L6 6.4 0.8 3z"/></svg>
        info@qlsummit.com
      </li>
    </ul>
  </div>
</section>

</body>
</html>
```